2018 Vision Board Workshop

I need to promote this workshop on both an 8.5x11 sheet and a 5x7 card. I do have a logo that needs to be present. I'd like to stay true to my branded colors. The flyer needs to project the excitement of a new year and the possibilities of what a person can create, produce, explore in their lives by putting it all on a vision board. Creating the vision of what you want will inspire you to achieve your goals and dreams. Looking at your vision board each day will propel you into taking action as you chart your course to achieve what you truly want.
The flyer needs to have the following information:
The workshop date and time - Sat., Jan. 13, 2018, 10:30-1:30
The location is - Atrium 47B, 2864 Birchwood Vale Rd, Colorado Springs, Co 80417
in the FORGE Room
My name and contact information - Mara Vollbeck
Text and voice 303-417-6652
Email - mara@brightwell-daily-craft.com
Website - brightwell-daily-craft.com
The fee is $45. All materials are provided.

My company is called Brightwell Daily Craft. I am a Life Coach, author, speaker and workshop leader.\ I wrote this program, Brightwell Daily Craft to teach concepts and supporting skills for living with more happiness, satisfaction and fulfillment. Thanks for reading this!! Mara

Target Market(s)

Primarily women, educated, motivated, proactive in their own lives and well being

Font styles to use
Other font styles liked:
• I have been using Century Gothic. I'm open to new ideas.

Requirements
Must have
• The Brightwell Daily Craft logo
• The flyer needs to have the following information:
• The workshop date and time - Sat., Jan. 13, 2018, 10:30-1:30
• The location is - Atrium 47B, 2864 Birchwood Vale Rd, Colorado Springs, Co 80417
• in the FORGE Room
• My name and contact information - Mara Vollbeck
• Text and voice 303-417-6652
• Email - mara@brightwell-daily-craft.com
• Website - brightwell-daily-craft.com
• The fee is $45. All materials are provided.
Nice to have
• The Brightwell Daily Craft branded colors in the design
• Images of vision boards

```html
<!DOCTYPE html>
<html lang="en">
<head>
<meta charset="utf-8">
<title>Vision Board Workshop – Brightwell Daily Craft</title>
<link rel="stylesheet" href="https://fonts.googleapis.com/css2?family=Montserrat:wght@400;500;700;800;900&display=swap">
<style>
  :root {
    --navy: #24418f;
    --navy-deep: #1b3170;
    --blue: #1f6fd1;
    --green: #8dc63f;
    --green-deep: #6aa82a;
    --ink: #2b2b2b;
    --cream: #fdf5dc;
    --paper: #ffffff;
  }
  html, body {
    margin: 0;
    padding: 0;
    width: 960px;
    height: 1200px;
    overflow: hidden;
    background: var(--paper);
  }
  .flyer {
    position: relative;
    width: 960px;
    height: 1200px;
    overflow: hidden;
    font-family: "Montserrat", sans-serif;
    color: var(--ink);
    background:
      radial-gradient(ellipse 70% 45% at 55% 55%, var(--cream) 0%, rgba(253,245,220,0) 100%),
      linear-gradient(180deg, #ffffff 0%, #fefaee 45%, #fdf6e2 100%);
  }
  .brand {
    position: absolute;
    top: 92px;
    left: 0;
    width: 960px;
    text-align: center;
  }
  .brand-name {
    display: inline-flex;
    align-items: center;
    gap: 12px;
    font-size: 40px;
    font-weight: 400;
    color: var(--green);
    letter-spacing: 0.5px;
  }
  .brand-dot {
    width: 18px;
    height: 18px;
    border-radius: 50%;
    background: var(--blue);
  }
  .brand-tagline {
    margin-top: 4px;
    padding-left: 110px;
    font-size: 17px;
    color: var(--blue);
    letter-spacing: 0.5px;
  }
  .headline {
    position: absolute;
    top: 214px;
    left: 150px;
    width: 660px;
    height: 420px;
  }
  .intro {
    position: absolute;
    top: 648px;
    left: 80px;
    width: 800px;
    margin: 0;
    text-align: center;
    font-size: 17.5px;
    line-height: 26px;
    color: #2a2a2a;
  }
  .date {
    position: absolute;
    top: 748px;
    left: 92px;
    width: 240px;
    height: 210px;
  }
  .date-day {
    position: absolute;
    top: 0;
    left: 4px;
    font-size: 26px;
    line-height: 30px;
    font-weight: 700;
    color: var(--green);
  }
  .date-num {
    position: absolute;
    top: 12px;
    left: 0;
    font-size: 136px;
    line-height: 1;
    font-weight: 900;
    letter-spacing: -6px;
    color: var(--navy);
  }
  .date-month {
    position: absolute;
    top: 136px;
    left: 4px;
    padding: 0 6px;
    border: 2px solid var(--navy);
    font-size: 26px;
    line-height: 28px;
    font-weight: 500;
    letter-spacing: 2px;
    color: var(--navy);
    background: #fff;
  }
  .date-time {
    position: absolute;
    top: 172px;
    left: 6px;
    display: flex;
    align-items: center;
    gap: 6px;
    font-size: 32px;
    line-height: 38px;
    font-weight: 700;
    color: var(--green);
    white-space: nowrap;
  }
  .date-year {
    position: absolute;
    top: 51px;
    left: 121px;
    width: 170px;
    height: 56px;
    transform: rotate(-90deg);
    transform-origin: center;
    text-align: center;
    font-size: 56px;
    font-weight: 900;
    line-height: 56px;
    color: var(--green);
  }
  .venue-arrow {
    position: absolute;
    top: 830px;
    left: 346px;
    width: 38px;
    height: 38px;
  }
  .venue {
    position: absolute;
    top: 776px;
    left: 370px;
    width: 508px;
    height: 138px;
    box-sizing: border-box;
    padding-top: 14px;
    border-radius: 14px;
    background: var(--navy);
    box-shadow: 0 3px 6px rgba(0,0,0,0.25);
    text-align: center;
    color: #e9eefb;
    font-size: 25px;
    line-height: 37px;
    font-style: normal;
  }
  .venue-room {
    font-weight: 800;
    color: var(--green);
    font-size: 27px;
  }
  .contact {
    position: absolute;
    top: 958px;
    left: 0;
    width: 960px;
    text-align: center;
  }
  .contact-label {
    display: inline-flex;
    align-items: center;
    gap: 8px;
    font-size: 16px;
    color: var(--navy);
  }
  .contact-label::before,
  .contact-label::after {
    content: "";
    width: 40px;
    height: 1.5px;
    background: var(--navy);
  }
  .contact-label span {
    padding: 1px 8px;
    border: 1px dashed var(--navy);
    border-radius: 10px;
  }
  .contact-name {
    margin: 2px 0 0;
    font-size: 40px;
    line-height: 50px;
    font-weight: 800;
    color: var(--navy-deep);
  }
  .contact-line {
    display: flex;
    justify-content: center;
    gap: 20px;
    margin-top: 4px;
    font-size: 20px;
    line-height: 28px;
    font-weight: 800;
    letter-spacing: -0.3px;
    color: var(--navy-deep);
    white-space: nowrap;
  }
  .contact-item {
    display: inline-flex;
    align-items: center;
    gap: 8px;
    white-space: nowrap;
  }
  .fee-band {
    position: absolute;
    top: 1126px;
    left: 0;
    width: 960px;
    height: 52px;
    background: var(--navy);
    color: #fff;
    display: flex;
    align-items: center;
    justify-content: center;
    gap: 38px;
    font-size: 30px;
    font-weight: 400;
    letter-spacing: 0.5px;
    white-space: nowrap;
  }
  .fee-band strong {
    font-weight: 900;
    font-size: 36px;
  }
  .fee-divider {
    width: 2px;
    height: 26px;
    background: #fff;
  }
</style>
</head>
<body>
<main class="flyer">

  <header class="brand">
    <div class="brand-name"><span class="brand-dot"></span>Brightwell Daily Craft</div>
    <div class="brand-tagline">What you think is what you create</div>
  </header>

  <svg class="headline" viewBox="0 0 660 420" role="img" aria-label="Headline lettering filled with a photo of smiling families: What you think is what you create">
    <defs>
      <linearGradient id="fill-navy" x1="0" y1="0" x2="1" y2="1">
        <stop offset="0" stop-color="#1b3170"/>
        <stop offset="1" stop-color="#2a5cb0"/>
      </linearGradient>
      <linearGradient id="fill-green" x1="0" y1="0" x2="1" y2="1">
        <stop offset="0" stop-color="#6f8f2a"/>
        <stop offset="0.5" stop-color="#8dc63f"/>
        <stop offset="1" stop-color="#5e9a22"/>
      </linearGradient>
      <linearGradient id="fill-blue" x1="0" y1="0" x2="1" y2="0">
        <stop offset="0" stop-color="#1f6fd1"/>
        <stop offset="1" stop-color="#1d4fa8"/>
      </linearGradient>
    </defs>
    <text x="6" y="88" textLength="648" lengthAdjust="spacingAndGlyphs" font-family="Montserrat, sans-serif" font-weight="900" font-size="104" fill="url(#fill-navy)">WHAT YOU</text>
    <text x="14" y="228" textLength="630" lengthAdjust="spacingAndGlyphs" font-family="Montserrat, sans-serif" font-weight="900" font-size="180" fill="url(#fill-green)">THINK</text>
    <text x="14" y="295" textLength="626" lengthAdjust="spacingAndGlyphs" font-family="Montserrat, sans-serif" font-weight="900" font-size="86" fill="url(#fill-blue)">IS WHAT YOU</text>
    <text x="10" y="410" textLength="634" lengthAdjust="spacingAndGlyphs" font-family="Montserrat, sans-serif" font-weight="900" font-size="148" fill="url(#fill-green)">CREATE</text>
  </svg>

  <p class="intro">The vision of what you want will inspire you to achieve your goals and dreams.<br>Looking at your vision board each day will propel you into taking action as you chart<br>your course to achieve what you truly want.</p>

  <section class="date">
    <div class="date-day">SATURDAY</div>
    <div class="date-num">13</div>
    <div class="date-month">JANUARY</div>
    <div class="date-time">
      <svg width="26" height="26" viewBox="0 0 26 26" aria-hidden="true">
        <circle cx="13" cy="14" r="9" fill="none" stroke="#24418f" stroke-width="3"/>
        <path d="M13 9v5l3 2" stroke="#24418f" stroke-width="2.5" fill="none" stroke-linecap="round"/>
        <path d="M4 6l4-3M22 6l-4-3" stroke="#24418f" stroke-width="2.5" stroke-linecap="round"/>
      </svg>
      10:30-1:30
    </div>
    <div class="date-year">2018</div>
  </section>

  <svg class="venue-arrow" viewBox="0 0 36 36" aria-hidden="true">
    <circle cx="18" cy="18" r="18" fill="#8dc63f"/>
    <path d="M15 11l7 7-7 7" fill="none" stroke="#fff" stroke-width="2.5" stroke-linecap="round" stroke-linejoin="round"/>
  </svg>
  <address class="venue">
    Atrium 47B, 2864 Birchwood Vale Rd,<br>
    Colorado Springs, Co 80417<br>
    <span class="venue-room">IN THE FORGE ROOM</span>
  </address>

  <section class="contact">
    <div class="contact-label"><span>Contact Information</span></div>
    <h2 class="contact-name">MARA VOLLBECK</h2>
    <div class="contact-line">
      <span class="contact-item">
        <svg width="20" height="20" viewBox="0 0 20 20" aria-hidden="true"><circle cx="10" cy="10" r="10" fill="#1b3170"/><path d="M7 5l2 3-1 1.5c.7 1.4 1.6 2.3 3 3L12.5 11l3 2-1 2c-4 0-8.5-4.5-8.5-8.5z" fill="#fff"/></svg>
        303-417-6652
      </span>
    </div>
    <div class="contact-line">
      <span class="contact-item">
        <svg width="22" height="22" viewBox="0 0 22 22" aria-hidden="true"><circle cx="11" cy="11" r="11" fill="#1b3170"/><rect x="5" y="7" width="12" height="8" rx="1" fill="#fff"/><path d="M5 7.5l6 4 6-4" fill="none" stroke="#1b3170" stroke-width="1.3"/></svg>
        MARA@BRIGHTWELL-DAILY-CRAFT.COM
      </span>
      <span class="contact-item">
        <svg width="20" height="20" viewBox="0 0 20 20" aria-hidden="true"><circle cx="10" cy="10" r="9" fill="#1b3170"/><g fill="none" stroke="#fff" stroke-width="1.2"><circle cx="10" cy="10" r="6"/><ellipse cx="10" cy="10" rx="2.6" ry="6"/><path d="M4 10h12"/></g></svg>
        BRIGHTWELL-DAILY-CRAFT.COM
      </span>
    </div>
  </section>

  <footer class="fee-band">
    <span>The fee is <strong>$45.</strong></span>
    <span class="fee-divider"></span>
    <span>ALL MATERIALS ARE PROVIDED</span>
  </footer>

</main>
</body>
</html>
```